Marlow Crest Group (Real Estate and Investment)

A high end, clean design.
We are a real estate company with sales, asset management and investment divisions. We want to use a black and white scheme which is really high end feel. The back of the card can just be the logo (black background with the white writing) as we will probably emboss this when we print)

Target Market(s)

High level investors, high end houses for sale

Industry/Entity Type

Business

Contact Information for Business Card

Name, position, phone number and email address
Glen Varley, Managing Director, 0437259064 and glen@marlowcrest-example.com.au

Requirements
Must have
• Back of the card to be the black background with the white writing (as per the attached images). Would like the capacity to emboss the writing and logo

```html
<!DOCTYPE html>
<html lang="en">
<head>
<meta charset="utf-8">
<title>Marlow Crest Group — Business Card</title>
<link href="https://fonts.googleapis.com/css2?family=Open+Sans:wght@300;400;700&display=swap" rel="stylesheet">
<style>
  :root {
    --canvas: #e9e9e7;
    --card-white: #ffffff;
    --card-black-top: #3a3939;
    --card-black-bottom: #232222;
    --ink: #1d1d1d;
    --ink-soft: #555555;
    --rule: #9a9a9a;
    --ghost: #f1f1f1;
    --paper-white: #ffffff;
  }
  * { box-sizing: border-box; margin: 0; padding: 0; }
  html, body {
    width: 1200px; height: 1200px; overflow: hidden;
    background: var(--canvas);
    font-family: "Open Sans", Arial, sans-serif;
  }
  .sheet {
    width: 1200px; height: 1200px;
    display: flex; flex-direction: column;
    align-items: center; justify-content: center; gap: 60px;
  }
  .card {
    position: relative;
    width: 800px; height: 457px;
    overflow: hidden;
    box-shadow: 0 10px 30px rgba(0,0,0,0.12);
  }

  /* Front */
  .card--front { background: var(--card-white); color: var(--ink); }
  .card__ghost-mark {
    position: absolute; right: 70px; top: 110px;
    width: 330px; height: 330px; border-radius: 50%;
    border: 3px solid var(--ghost);
  }
  .brand {
    position: absolute; left: 60px; top: 52px;
    display: flex; align-items: center; gap: 18px;
  }
  .brand__dot {
    width: 64px; height: 64px; border-radius: 50%;
    border: 2px solid var(--ink);
    flex: none;
  }
  .brand__name {
    font-weight: 400; font-size: 26px; letter-spacing: 1px;
    text-transform: uppercase; color: var(--ink);
  }
  .person {
    position: absolute; left: 60px; top: 176px;
    width: 300px;
  }
  .person__name {
    font-weight: 700; font-size: 32px; letter-spacing: 0.5px;
    text-transform: uppercase; line-height: 1.1;
  }
  .person__role {
    font-weight: 400; font-size: 18px; color: var(--ink-soft);
    margin-top: 4px; padding-bottom: 12px;
    border-bottom: 1px solid var(--rule);
  }
  .contact {
    position: absolute; left: 60px; top: 270px; right: 60px;
    display: flex; align-items: center; gap: 8px;
    font-size: 13px; color: var(--ink-soft);
    padding-bottom: 12px; border-bottom: 1px solid var(--rule);
    white-space: nowrap;
  }
  .contact__item { display: flex; align-items: center; gap: 6px; }
  .contact__sep { color: var(--ink-soft); }
  .contact svg { width: 14px; height: 14px; flex: none; fill: none; stroke: var(--ink); stroke-width: 1.8; }
  .contact svg .solid { fill: var(--ink); stroke: none; }

  /* Back */
  .card--back {
    background: linear-gradient(160deg, var(--card-black-top), var(--card-black-bottom));
    display: flex; align-items: center; justify-content: center;
  }
  .brand--back { position: static; flex-direction: column; gap: 22px; }
  .brand--back .brand__dot { width: 90px; height: 90px; border-color: var(--paper-white); }
  .brand--back .brand__name { color: var(--paper-white); font-size: 32px; letter-spacing: 2px; }
</style>
</head>
<body>
  <main class="sheet">
    <section class="card card--front" aria-label="Business card front">
      <div class="card__ghost-mark"></div>
      <div class="brand">
        <span class="brand__dot"></span>
        <span class="brand__name">Marlow Crest Group</span>
      </div>
      <div class="person">
        <h1 class="person__name">Glen Varley</h1>
        <p class="person__role">Managing Director</p>
      </div>
      <div class="contact">
        <span class="contact__item">
          <svg viewBox="0 0 24 24" aria-hidden="true"><path class="solid" d="M6.6 10.8a15 15 0 0 0 6.6 6.6l2.2-2.2a1 1 0 0 1 1-.25 11.4 11.4 0 0 0 3.6.57 1 1 0 0 1 1 1V20a1 1 0 0 1-1 1A17 17 0 0 1 3 4a1 1 0 0 1 1-1h3.5a1 1 0 0 1 1 1c0 1.250.2 2.450.57 3.570a1 1 0 0 1-.25 1z"/></svg>
          0437259064
        </span>
        <span class="contact__sep">|</span>
        <span class="contact__item">
          <svg viewBox="0 0 24 24" aria-hidden="true"><rect x="3" y="5" width="18" height="14" rx="1"/><path d="M3 6l9 7 9-7"/></svg>
          glen@marlowcrest-example.com.au
        </span>
        <span class="contact__sep">|</span>
        <span class="contact__item">
          <svg viewBox="0 0 24 24" aria-hidden="true"><circle cx="12" cy="12" r="9"/><path d="M3 12h18M12 3c3 3 3 15 0 18M12 3c-3 3-3 15 0 18"/></svg>
          www.marlowcrest-example.com.au
        </span>
      </div>
    </section>

    <section class="card card--back" aria-label="Business card back">
      <div class="brand brand--back">
        <span class="brand__dot"></span>
        <span class="brand__name">Marlow Crest Group</span>
      </div>
    </section>
  </main>
</body>
</html>
```